The Steel Hand Close Quarters Protocol Cover

Hi we are producing a self defense course entitled The Steel Hand Close Quarters Protocol: A Complete Field Manual For Commanding The Blade Every Operator Trusts Above Any Other Tool.

I listed this as a book cover but it will actually be a DVD set, but the book cover model works fine.

See below for design examples - I am thinking we need a cover that will appeal to military/survival type people.

Target Market(s)

survivalists, cops, preppers, gun owners, martial artists, and average people wanting to learn how to defend themselves

Industry/Entity Type

Defense

Requirements
Must have
• Title: THE STEEL HAND CLOSE QUARTERS PROTOCOL: A COMPLETE FIELD MANUAL FOR COMMANDING THE BLADE EVERY OPERATOR TRUSTS ABOVE ANY OTHER TOOL
Nice to have
• Please look at these sample designs from other books as a model:
• https://files.pelorvane-archive.example/covers/4/27/MarlowGrayfield.jpg - This stye is ideal.
• Other good examples:
• https://media2.quillorbit.example/8841027_k390.jpg
• http://c.tovenreads.example/titles/1289045517m/48102936.jpg
• http://img.brisketmart.example/pics/P/73Rt82MqWnB._XZ_QT410_LM305,410_.jpg
• http://3.cdn.jottlepage.example/-MRtYVVKDDQ/BWNs_harpoQ/BBBBBBBBx9K/TRPk418WpXZ/s1600/Q3408817.JPG

```html
<!DOCTYPE html>
<html lang="en">
<head>
<meta charset="utf-8">
<title>The Steel Hand Close Quarters Protocol Cover</title>
<link rel="stylesheet" href="https://fonts.googleapis.com/css2?family=Black+Ops+One&family=Permanent+Marker&family=Montserrat:wght@400;500&display=swap">
<style>
  :root {
    --page-bg: #2b2b2d;
    --band-gold: #a38b3c;
    --band-gold-dark: #7f6a2a;
    --cover-brown: #3b2b20;
    --cover-brown-dark: #241a14;
    --title-ink: #e9ece6;
    --blade-steel: #56747a;
    --blade-steel-dark: #3e5559;
    --author-red: #c9262a;
    --publisher-ink: #bdb6ad;
  }
  * { margin: 0; padding: 0; box-sizing: border-box; }
  html, body { width: 1200px; height: 1000px; overflow: hidden; }
  body {
    background: var(--page-bg);
    display: flex;
    align-items: center;
    justify-content: center;
  }
  .cover {
    position: relative;
    width: 680px;
    height: 920px;
    background: radial-gradient(ellipse at 50% 40%, var(--cover-brown) 0%, var(--cover-brown-dark) 100%);
    box-shadow: 0 10px 30px rgba(0,0,0,.5);
    overflow: hidden;
  }
  .title-band {
    height: 300px;
    background: linear-gradient(160deg, var(--band-gold) 0%, var(--band-gold-dark) 100%);
    text-align: center;
    padding-top: 26px;
  }
  .title-lead {
    font-family: "Black Ops One", sans-serif;
    font-size: 36px;
    line-height: 1.15;
    color: var(--title-ink);
    text-shadow: 2px 2px 0 rgba(0,0,0,.45);
    letter-spacing: 1px;
  }
  .title-main {
    font-family: "Black Ops One", sans-serif;
    font-size: 108px;
    line-height: 1.1;
    color: var(--title-ink);
    text-shadow: 3px 4px 0 rgba(0,0,0,.4);
    letter-spacing: 2px;
    white-space: nowrap;
  }
  .blade-art {
    position: absolute;
    height: 90px;
    width: 500px;
    background: linear-gradient(180deg, var(--blade-steel) 0%, var(--blade-steel-dark) 100%);
  }
  .blade-art.upper { top: 340px; left: 40px; border-radius: 45px 8px 8px 45px; }
  .blade-art.lower { top: 655px; left: 140px; border-radius: 8px 45px 45px 8px; }
  .subtitle {
    position: absolute;
    top: 465px;
    left: 20px;
    right: 20px;
    text-align: center;
    font-family: "Permanent Marker", sans-serif;
    font-weight: 400;
    color: var(--title-ink);
    line-height: 1.05;
    white-space: nowrap;
  }
  .subtitle .sub-large { display: block; font-size: 38px; letter-spacing: 1px; }
  .subtitle .sub-small { display: block; font-size: 18px; margin: 3px 0 5px; }
  .author {
    position: absolute;
    top: 790px;
    left: 0; right: 0;
    text-align: center;
    font-family: "Montserrat", sans-serif;
    font-weight: 400;
    font-size: 44px;
    letter-spacing: 6px;
    color: var(--author-red);
    white-space: nowrap;
  }
  .publisher {
    position: absolute;
    top: 872px;
    left: 0; right: 0;
    text-align: center;
    font-family: "Montserrat", sans-serif;
    font-weight: 500;
    font-size: 10px;
    letter-spacing: 4px;
    color: var(--publisher-ink);
  }
</style>
</head>
<body>
  <main class="cover">
    <header class="title-band">
      <p class="title-lead">THE STEEL HAND<br>CLOSE QUARTERS</p>
      <h1 class="title-main">PROTOCOL</h1>
    </header>

    <div class="blade-art upper" role="img" aria-label="Illustration of a combat knife with serrated spine, blade pointing left"></div>

    <h2 class="subtitle">
      <span class="sub-large">A COMPLETE FIELD MANUAL</span>
      <span class="sub-small">FOR COMMANDING THE BLADE EVERY OPERATOR</span>
      <span class="sub-large">TRUSTS ABOVE</span>
      <span class="sub-small">ANY OTHER TOOL.</span>
    </h2>

    <div class="blade-art lower" role="img" aria-label="Illustration of a combat knife with ridged grip, blade pointing right"></div>

    <p class="author">DANE R. CORWELL</p>
    <p class="publisher">IRONSIDE TRAIL VIDEO</p>
  </main>
</body>
</html>
```